Q & Q Fabrications HVAC Mechanical Contractor Business Card

We need a business card for a HVAC/Plumbing Mechanical Contractor. Our website is http://www.qqfabrications-example.com. We would like to include the picture of the person on the card. Pictures of people for mock-ups can be found on our website. The blue on our logo is our primary color. We'd like this to be bold yet professional without too many colors but with some color to make sure it stands out.

Industry/Entity Type

Business

Contact Information for Business Card

Font styles to use
Sans Serif

Colors
000000

Requirements
Must have
• Our logo
• Person's picture
• Company Name
• Company Phone
• Person's email address
• Person's phone number
Nice to have
• Company Address
Should not have
• Clip art

```html
<!DOCTYPE html>
<html lang="en">
<head>
<meta charset="utf-8">
<title>Q &amp; Q Fabrications – Business Card</title>
<link rel="stylesheet" href="https://fonts.googleapis.com/css2?family=Bebas+Neue&family=Oswald:wght@300;400&display=swap">
<style>
  :root {
    --blue-dark: #2f6db8;
    --blue-mid: #3596d4;
    --blue-light: #7cc6ef;
    --ink: #1c1c1c;
    --paper: #ffffff;
    --photo-top: #8a8d90;
    --photo-bottom: #4a4d52;
  }
  html, body {
    margin: 0;
    padding: 0;
    width: 1200px;
    height: 667px;
    overflow: hidden;
    background: var(--paper);
  }
  .card {
    position: relative;
    width: 1200px;
    height: 667px;
    background: var(--paper);
    overflow: hidden;
    color: var(--ink);
  }
  .side-band { position: absolute; left: 0; top: 0; width: 100px; height: 667px; }
  .corner-circles { position: absolute; right: 0; top: 320px; width: 70px; height: 347px; }

  .brand-mark {
    position: absolute;
    left: 122px; top: 98px;
    width: 344px; height: 187px;
    display: flex; align-items: center; gap: 22px;
  }
  .brand-square { width: 120px; height: 120px; background: var(--blue-dark); flex: none; }
  .brand-initials {
    font-family: "Bebas Neue", sans-serif;
    font-size: 96px; line-height: 1; color: var(--ink);
  }
  .company-name {
    position: absolute; left: 118px; top: 304px; margin: 0;
    font-family: "Bebas Neue", sans-serif; font-weight: 400;
    font-size: 48px; line-height: 1; letter-spacing: 0.5px; color: var(--ink);
  }
  .company-trade {
    position: absolute; left: 124px; top: 366px; margin: 0;
    font-family: "Bebas Neue", sans-serif;
    font-size: 38px; line-height: 1; color: var(--ink);
  }

  .person {
    position: absolute; right: 250px; top: 108px; text-align: right;
  }
  .person-name {
    margin: 0;
    font-family: "Bebas Neue", sans-serif; font-weight: 400;
    font-size: 62px; line-height: 0.9; color: var(--ink);
  }
  .person-title {
    margin: 10px 0 0;
    font-family: "Bebas Neue", sans-serif;
    font-size: 30px; line-height: 1; color: var(--ink);
  }
  .portrait {
    position: absolute; left: 969px; top: 98px;
    width: 186px; height: 187px; box-sizing: border-box;
    border: 10px solid var(--blue-light);
    background: linear-gradient(160deg, var(--photo-top), var(--photo-bottom));
  }

  .contacts {
    position: absolute; top: 466px; left: 122px;
    display: grid; grid-template-columns: 486px 260px;
    column-gap: 0; row-gap: 20px;
    list-style: none; margin: 0; padding: 0;
  }
  .contact {
    display: flex; align-items: center; gap: 16px;
    font-family: "Oswald", sans-serif; font-weight: 300;
    font-size: 26px; line-height: 36px; color: var(--ink);
    white-space: nowrap;
    min-width: 0;
  }
  .contact svg { width: 32px; height: 32px; flex: none; }
</style>
</head>
<body>
<main class="card">
  <svg class="side-band" viewBox="0 0 100 667" aria-hidden="true">
    <rect x="0" y="0" width="66" height="223" fill="var(--blue-dark)"/>
    <rect x="0" y="222" width="66" height="223" fill="var(--blue-mid)"/>
    <polygon points="66,305 99,328 66,351" fill="var(--blue-mid)"/>
    <rect x="0" y="444" width="66" height="223" fill="var(--blue-light)"/>
  </svg>

  <svg class="corner-circles" viewBox="0 0 70 347" aria-hidden="true">
    <circle cx="120" cy="110" r="110" fill="var(--blue-dark)"/>
    <circle cx="110" cy="195" r="85" fill="var(--blue-mid)"/>
    <circle cx="115" cy="300" r="105" fill="var(--blue-light)"/>
  </svg>

  <div class="brand-mark">
    <span class="brand-square"></span>
    <span class="brand-initials">Q &amp; Q</span>
  </div>
  <h1 class="company-name">Q &amp; Q Fabrications, Inc</h1>
  <p class="company-trade">Mechanical Contractor</p>

  <div class="person">
    <h2 class="person-name">Daniel<br>Marstrand</h2>
    <p class="person-title">CEO / Project Manager</p>
  </div>
  <div class="portrait" role="img" aria-label="Portrait photo of Daniel Marstrand"></div>

  <ul class="contacts">
    <li class="contact">
      <svg viewBox="0 0 32 32" aria-hidden="true"><circle cx="16" cy="16" r="14.5" fill="none" stroke="var(--ink)" stroke-width="1.5"/><path d="M16 8a5 5 0 0 0-5 5c0 4 5 10 5 10s5-6 5-10a5 5 0 0 0-5-5zm0 7a2 2 0 1 1 0-4 2 2 0 0 1 0 4z" fill="var(--ink)"/></svg>
      1450 Birch Road, Fairview, WI 53000-1200
    </li>
    <li class="contact">
      <svg viewBox="0 0 32 32" aria-hidden="true"><circle cx="16" cy="16" r="14.5" fill="none" stroke="var(--ink)" stroke-width="1.5"/><path d="M10.5 11.5c.8-.8 1.5-.8 2 0l1.6 2.4c.4.6.2 1.2-.3 1.6l-.8.6c.8 1.8 2 3 3.8 3.8l.6-.8c.4-.5 1-.7 1.6-.3l2.4 1.6c.8.5.8 1.2 0 2l-1 1c-1 1-3.4.6-6.2-2.2s-3.2-5.2-2.2-6.2z" fill="none" stroke="var(--ink)" stroke-width="1.4"/></svg>
      +1-555-010-4477
    </li>
    <li class="contact">
      <svg viewBox="0 0 32 32" aria-hidden="true"><circle cx="16" cy="16" r="14.5" fill="none" stroke="var(--ink)" stroke-width="1.5"/><rect x="9.5" y="11.5" width="13" height="9" fill="var(--ink)"/><path d="M9.5 11.5l6.5 5 6.5-5" fill="none" stroke="var(--paper)" stroke-width="1.2"/></svg>
      dmarstrand@qqfabrications-example.com
    </li>
    <li class="contact">
      <svg viewBox="0 0 32 32" aria-hidden="true"><circle cx="16" cy="16" r="14.5" fill="none" stroke="var(--ink)" stroke-width="1.5"/><rect x="12" y="8.5" width="8" height="15" rx="1.5" fill="none" stroke="var(--ink)" stroke-width="1.4"/><circle cx="16" cy="21" r="0.9" fill="var(--ink)"/></svg>
      +1-555-010-4478
    </li>
    <li class="contact">
      <svg viewBox="0 0 32 32" aria-hidden="true"><circle cx="16" cy="16" r="14.5" fill="none" stroke="var(--ink)" stroke-width="1.5"/><circle cx="16" cy="16" r="7" fill="none" stroke="var(--ink)" stroke-width="1.4"/><path d="M9 16h14M16 9c-3 3.5-3 10.5 0 14M16 9c3 3.5 3 10.5 0 14" fill="none" stroke="var(--ink)" stroke-width="1.2"/></svg>
      www.qqfabrications-example.com
    </li>
    <li class="contact">
      <svg viewBox="0 0 32 32" aria-hidden="true"><circle cx="16" cy="16" r="14.5" fill="var(--ink)"/><rect x="11.5" y="8.5" width="9" height="5" fill="var(--paper)"/><rect x="8.5" y="13" width="15" height="7" rx="1" fill="var(--paper)"/><rect x="11.5" y="17.5" width="9" height="6" fill="var(--paper)" stroke="var(--ink)" stroke-width="1"/></svg>
      +1-555-010-4479
    </li>
  </ul>
</main>
</body>
</html>
```